Quote Cards With TK May 2025 for Instagram

I would like to put these quotes over one of the pictures attached; Instagram (new size: 4:5 (1080 x 1350 pixels) One Quote per picture, and I want the quote to be bold or easy to read as well. I provided a few reference graphics that I really like as examples below. In very small letters at the bottom add @TKBarlowOnline

All of the pictures are attached; you can pick any photo and add one quote to it; but no stock photography

```html
<!DOCTYPE html>
<html lang="en">
<head>
<meta charset="utf-8">
<title>Quote Cards – TK – May 2025</title>
<link href="https://fonts.googleapis.com/css2?family=Poppins:wght@300;400;500;600&display=swap" rel="stylesheet">
<style>
:root{
  --page:#fdeef7;
  --pink-soft:#fbc8e3;
  --pink-hot:#ff3d98;
  --magenta:#d4076c;
  --magenta-text:#e0197d;
  --white:#ffffff;
  --ink:#222;
}
*{box-sizing:border-box;margin:0;padding:0}
html,body{width:781px;height:1200px;overflow:hidden;background:var(--page)}
body{position:relative;font-family:"Poppins",sans-serif;color:var(--white)}
.card{position:absolute;width:211px;height:264px;overflow:hidden}
.photo{position:absolute;inset:0}
.col-1{left:65px}.col-2{left:285px}.col-3{left:505px}
.row-1{top:53px}.row-2{top:330px}.row-3{top:607px}.row-4{top:884px}
.txt{position:absolute;line-height:1.02}
.kicker{font-size:7px;font-weight:500}
.big{font-size:19px;font-weight:300}
.mid{font-size:11.5px;font-weight:300}
.center{text-align:center;left:8px;right:8px}
.handle{position:absolute;font-size:6px;font-weight:500;letter-spacing:1.2px}
b{font-weight:600}
.arc{position:absolute;border-radius:50%}
.frame{position:absolute;border:0.6px solid rgba(255,180,220,.7)}
.band{position:absolute;left:0;right:0}
</style>
</head>
<body>

<!-- Card 1 -->
<section class="card col-1 row-1" style="background:var(--white)">
  <div class="photo" style="left:105px" role="img" aria-label="Woman in a sheer black striped top standing in a kitchen" >
    <div style="position:absolute;inset:0;background:linear-gradient(180deg,#6e5a4e 0%,#3a2d28 45%,#141111 100%)"></div>
  </div>
  <div class="arc" style="width:70px;height:70px;right:-22px;top:-30px;border:14px solid var(--pink-soft)"></div>
  <div class="arc" style="width:40px;height:40px;left:-18px;bottom:-18px;border:8px solid var(--pink-soft)"></div>
  <p class="txt" style="left:10px;top:23px;width:92px;font-size:11.5px;color:var(--magenta-text);line-height:.98">Tired. Moody. Stubborn Belly Fat. Your hormones are screaming for help!</p>
  <p class="txt" style="left:10px;top:103px;font-size:19px;color:var(--magenta-text);line-height:1">Let’s fix<br>that.</p>
  <span class="handle" style="left:10px;bottom:15px;color:var(--ink)">@TKBarlowOnline</span>
</section>

<!-- Card 2 -->
<section class="card col-2 row-1">
  <div class="photo" role="img" aria-label="Smiling woman in black outfit on a hillside overlook" style="background:linear-gradient(180deg,#9fb0b6 0%,#7d8a7c 40%,#3e4a33 70%,#1c1c1c 100%)"></div>
  <div class="arc" style="width:50px;height:50px;right:-20px;top:-22px;border:10px solid var(--pink-soft)"></div>
  <p class="txt kicker" style="left:10px;top:131px">That stubborn weight?</p>
  <p class="txt big" style="left:10px;top:143px">It’s not<br>your fault.</p>
  <p class="txt mid" style="left:10px;top:194px;width:140px;line-height:1.02">Your hormones are to blame and you’re not alone; But there is a fix.</p>
  <span class="handle" style="left:10px;bottom:15px">@TKBarlowOnline</span>
  <svg style="position:absolute;left:84px;bottom:16px" width="122" height="4"><circle cx="2" cy="2" r="1.6" fill="#fff"/><line x1="6" y1="2" x2="122" y2="2" stroke="#fff" stroke-width=".4" opacity=".6"/></svg>
</section>

<!-- Card 3 -->
<section class="card col-3 row-1">
  <div class="photo" role="img" aria-label="Woman in pink cropped sweater dancing in a kitchen" style="background:linear-gradient(180deg,#b794ae 0%,#9a7897 45%,#6f5670 100%)"></div>
  <div class="arc" style="width:116px;height:116px;left:47px;bottom:-60px;border:8px solid var(--magenta);border-bottom-color:transparent"></div>
  <p class="txt kicker center" style="top:109px">Your belly isn’t fat… it’s hormonal.</p>
  <p class="txt big center" style="top:120px">And here’s how<br>to fix it.</p>
  <p class="txt mid center" style="top:169px">Comment <b>HORMONES</b><br>if nothing is working.</p>
  <span class="handle center" style="bottom:15px;text-align:center">@TKBarlowOnline</span>
</section>

<!-- Card 4 -->
<section class="card col-1 row-2">
  <div class="photo" role="img" aria-label="Woman in a pink gown in front of a neon light backdrop" style="background:linear-gradient(100deg,#2b2f8a 0%,#7a3a9a 30%,#ff6a2a 55%,#b02a8a 75%,#2a2a6a 100%)"></div>
  <div class="frame" style="left:14px;top:14px;right:16px;bottom:18px"></div>
  <p class="txt kicker" style="right:25px;top:156px">The stubborn belly fat after 40?</p>
  <p class="txt mid" style="right:25px;top:169px;text-align:right">It’s not about calories; it’s<br>about your hormones.</p>
  <p class="txt big" style="right:26px;top:202px">Here is the fix!</p>
  <span class="handle" style="right:15px;bottom:15px">● @TKBarlowOnline</span>
</section>

<!-- Card 5 -->
<section class="card col-2 row-2">
  <div class="photo" role="img" aria-label="Woman in a shimmering brown top on a basketball court" style="background:linear-gradient(180deg,#3a3850 0%,#6a5a50 35%,#9a7a50 60%,#b9902f 100%)"></div>
  <div class="frame" style="left:14px;top:14px;right:14px;bottom:30px;border-color:rgba(212,7,108,.6)"></div>
  <div class="arc" style="width:72px;height:72px;right:-24px;top:-26px;border:15px solid var(--pink-hot)"></div>
  <div class="arc" style="width:40px;height:40px;left:-12px;bottom:-20px;border:8px solid var(--pink-soft)"></div>
  <p class="txt kicker center" style="top:133px">Flat tummy in your 40s?</p>
  <p class="txt big center" style="top:145px">It’s still possible!</p>
  <p class="txt mid center" style="top:183px">Comment <b>BYE BELLY</b><br>to get the 10 secrets to a<br>flatter tummy.</p>
  <div class="band" style="top:233px;height:20px;background:var(--white)"></div>
  <span class="handle center" style="top:240px;text-align:center;color:var(--ink)">@TKBarlowOnline</span>
</section>

<!-- Card 6 -->
<section class="card col-3 row-2">
  <div class="photo" role="img" aria-label="Woman in black outfit standing before green hills" style="background:linear-gradient(180deg,#a8b9c4 0%,#9aa28c 40%,#4d5a3a 75%,#26301f 100%)"></div>
  <div class="frame" style="left:10px;top:10px;right:10px;bottom:10px"></div>
  <p class="txt kicker center" style="top:158px">Bloating. Muffin top. Puffy waistline.</p>
  <p class="txt mid center" style="top:171px">Your body’s screaming for<br>a different kind of fix.</p>
  <p class="txt big center" style="top:204px">Here it is.</p>
  <div class="band" style="left:10px;right:10px;top:238px;height:15px;background:var(--pink-soft)"></div>
  <span class="handle center" style="top:242px;text-align:center;color:var(--magenta)">@TKBarlowOnline</span>
</section>

<!-- Card 7 -->
<section class="card col-1 row-3">
  <div class="photo" role="img" aria-label="Woman in pink outfit in a mirrored room with sunflowers" style="background:linear-gradient(180deg,#8a9aa8 0%,#a07a90 40%,#8a6a6a 70%,#a07a20 100%)"></div>
  <div class="band" style="top:0;height:10px;background:var(--pink-soft)"></div>
  <p class="txt mid center" style="top:120px">You’re doing all the “<b>right</b>”<br>things, but your belly won’t<br>go down?</p>
  <p class="txt big center" style="top:170px">Here’s what you<br>haven’t tried.</p>
  <span class="handle center" style="top:223px;text-align:center">@TKBarlowOnline</span>
</section>

<!-- Card 8 -->
<section class="card col-2 row-3">
  <div class="photo" role="img" aria-label="Woman in a black backless top looking over her shoulder" style="background:linear-gradient(180deg,#5a3a50 0%,#3c2634 45%,#4a2a3c 75%,#7a2a50 100%)"></div>
  <div class="band" style="top:0;height:10px;background:var(--magenta)"></div>
  <div class="arc" style="width:96px;height:96px;left:-28px;bottom:-52px;background:var(--magenta);border:9px solid var(--pink-soft)"></div>
  <div class="arc" style="width:110px;height:110px;left:44px;bottom:-90px;background:var(--pink-hot)"></div>
  <div class="arc" style="width:90px;height:90px;right:-30px;bottom:-46px;background:#b5002a;border:9px solid #ff8fc6"></div>
  <p class="txt mid center" style="top:145px">This 90-day plan helped women<br>over 40 slim down, get a tiny<br>waist and feel sexy again.</p>
  <p class="txt big center" style="top:186px">You’re next.</p>
  <span class="handle center" style="top:226px;text-align:center">@TKBarlowOnline</span>
</section>

<!-- Card 9 -->
<section class="card col-3 row-3">
  <div class="photo" role="img" aria-label="Woman in black sheer top in a high-rise apartment at night" style="background:linear-gradient(180deg,#4a4a5a 0%,#1e2a48 40%,#202030 75%,#3a3a3a 100%)"></div>
  <div class="arc" style="width:60px;height:60px;left:-26px;top:-28px;border:12px solid #e0409a"></div>
  <div class="arc" style="width:46px;height:46px;right:-14px;bottom:-20px;border:9px solid var(--pink-soft)"></div>
  <p class="txt mid" style="left:14px;top:118px;line-height:1.02">This is the secret women<br>over 40 are using to get<br>snatched; without starving.</p>
  <p class="txt big" style="left:14px;top:157px">Comment<br><b>SKINNY</b> to get<br>the exact plan.</p>
  <div class="band" style="top:234px;height:20px;background:var(--pink-hot)"></div>
  <span class="handle" style="left:14px;top:241px">@TKBarlowOnline</span>
</section>

<!-- Card 10 -->
<section class="card col-2 row-4">
  <div class="photo" role="img" aria-label="Woman in a sheer striped top dancing in a living room" style="background:linear-gradient(180deg,#6a5068 0%,#a07a98 40%,#7a5a78 75%,#5a4058 100%)"></div>
  <p class="txt mid" style="left:25px;top:100px">What worked in your 30s<br>won’t work now.</p>
  <p class="txt big" style="left:25px;top:133px;line-height:.98">Here’s what<br>actually does.<br>Drop 30 Pounds<br>in 3 Months.</p>
  <div class="band" style="left:25px;right:25px;top:230px;height:15px;background:var(--magenta)"></div>
  <span class="handle center" style="top:234px;text-align:center">@TKBarlowOnline</span>
</section>

</body>
</html>
```